Chicken Coop Sign

I would like to make a metal chicken coop sign in the size of 8 x 12 inches. The orientation can be vertical or horizontal.

I would like the designer to use any of these funny phrases and try and create a catchy graphic based on some of the designs that are already in the market.

"The Poultry Palace: Where Every Hen is a Queen"

"The Hen Den: No Foxes Allowed"

"The Eggsecutive Mansion"

"The Cluck Hut: No Fowl Moods Allowed"

"The Cluck and Fluff: Luxury Lodging for Hens"

Target Market(s)

Families that have chicken coops as a hobby in their backyard or farm.

Requirements
Must have
• It must be funny, use one of the provided quotes, have a "vintage" or "rustic" look
Nice to have
Should not have
• Stay away from 4 letter words like "SHIT", "FUCK" or Starred out works like "S**T" and "F**K"

```html
<!DOCTYPE html>
<html lang="en">
<head>
<meta charset="utf-8">
<title>The Cluck and Fluff – Coop Sign</title>
<link rel="stylesheet" href="https://fonts.googleapis.com/css2?family=Lilita+One&family=Alegreya+Sans:wght@700&family=Cinzel:wght@900&display=swap">
<style>
  :root {
    --backdrop: #e6e2dc;
    --sign-cream: #edcfa6;
    --sign-red: #e3222b;
    --title-cream: #f8e6c8;
    --ink: #2a2522;
    --wood-light: #a9848a;
    --wood-dark: #6d4a45;
    --hen-brown: #9b4a2a;
  }
  html, body {
    margin: 0;
    width: 1200px;
    height: 1117px;
    overflow: hidden;
    background: var(--backdrop);
  }
  .sign {
    position: absolute;
    left: 250px;
    top: 36px;
    width: 700px;
    height: 1045px;
    background: var(--sign-cream);
    box-shadow: 0 6px 18px rgba(0,0,0,0.18);
  }
  .sign__grunge {
    position: absolute;
    left: 0; top: 0;
    width: 700px; height: 660px;
  }
  .sign__title {
    position: absolute;
    left: 0; top: 40px;
    width: 700px;
    margin: 0;
    text-align: center;
    font-family: "Lilita One", "Arial Black", sans-serif;
    font-weight: 400;
    font-size: 132px;
    line-height: 116px;
    letter-spacing: -1px;
    color: var(--title-cream);
    text-shadow:
      -3px -3px 0 var(--ink), 3px -3px 0 var(--ink),
      -3px 3px 0 var(--ink), 3px 3px 0 var(--ink),
      7px 7px 0 var(--ink);
  }
  .sign__photo {
    position: absolute;
    left: 94px; top: 301px;
    width: 513px; height: 338px;
    background:
      radial-gradient(ellipse 22% 42% at 38% 52%, var(--hen-brown) 0 70%, transparent 100%),
      linear-gradient(135deg, var(--wood-light), var(--wood-dark));
  }
  .sign__tagline {
    position: absolute;
    left: 0; top: 680px;
    width: 700px;
    height: 70px;
  }
  .sign__tagline text {
    font-family: "Alegreya Sans", "Trebuchet MS", sans-serif;
    font-weight: 700;
    font-size: 46px;
    letter-spacing: 22px;
    fill: var(--ink);
  }
  .sign__subline {
    position: absolute;
    left: 0; top: 742px;
    width: 700px;
    margin: 0;
    text-align: center;
    font-family: "Alegreya Sans", "Trebuchet MS", sans-serif;
    font-weight: 700;
    font-size: 88px;
    line-height: 88px;
    color: var(--ink);
  }
  .sign__headline {
    position: absolute;
    left: 0; top: 810px;
    width: 700px;
    margin: 0;
    text-align: center;
    font-family: "Cinzel", Georgia, serif;
    font-weight: 900;
    font-size: 200px;
    line-height: 200px;
    letter-spacing: -6px;
    color: var(--sign-red);
  }
</style>
</head>
<body>
  <main class="sign">
    <svg class="sign__grunge" viewBox="0 0 700 660" aria-hidden="true">
      <defs>
        <filter id="rough-edge" x="-5%" y="-5%" width="110%" height="110%">
          <feTurbulence type="fractalNoise" baseFrequency="0.09" numOctaves="3" seed="4"/>
          <feDisplacementMap in="SourceGraphic" scale="16"/>
        </filter>
      </defs>
      <rect x="24" y="18" width="652" height="604" fill="var(--sign-red)" filter="url(#rough-edge)"/>
    </svg>

    <h1 class="sign__title">THE CLUCK<br>AND FLUFF</h1>

    <div class="sign__photo" role="img" aria-label="Photo of a brown hen stepping out of a small open wooden coop window"></div>

    <svg class="sign__tagline" viewBox="0 0 700 70" aria-label="Luxury">
      <path id="tagline-arc" d="M170 64 Q350 0 530 64" fill="none"/>
      <text text-anchor="middle"><textPath href="#tagline-arc" startOffset="51%">LUXURY</textPath></text>
    </svg>

    <p class="sign__subline">LODGING FOR</p>
    <p class="sign__headline">HENS</p>
  </main>
</body>
</html>
```